New residential property management company

I have a lot of name recognition in our smaller town due to owning a construction company here. I have now started a residential property management company representing landlords and tenants. Just trying to get my name out there and get some rentals to manage!

```html
<!DOCTYPE html>
<html lang="en">
<head>
<meta charset="utf-8">
<title>Halden Property Management – Postcard</title>
<link href="https://fonts.googleapis.com/css2?family=Oswald:wght@400;500;600&family=Roboto+Condensed:wght@700&family=Open+Sans:wght@400;600;700&display=swap" rel="stylesheet">
<style>
  :root{
    --yellow:#f7b516;
    --yellow-deep:#f2a90c;
    --ink:#1b1b1b;
    --charcoal:#333333;
    --grey:#555555;
    --rule:#cfcfcf;
    --paper:#ffffff;
    --backdrop:#e6e6e6;
  }
  *{margin:0;padding:0;box-sizing:border-box;}
  html,body{width:1088px;height:1200px;overflow:hidden;background:var(--backdrop);}
  .canvas{position:relative;width:1088px;height:1200px;}
  .card{position:absolute;left:166px;width:756px;height:474px;background:var(--paper);overflow:hidden;box-shadow:0 4px 14px rgba(0,0,0,.18);}
  .card--front{top:102px;}
  .card--back{top:624px;}
  .card svg.shapes{position:absolute;left:0;top:0;}
  .brand{position:absolute;display:flex;align-items:center;gap:12px;}
  .brand__mark{width:38px;height:38px;background:var(--ink);}
  .brand__text{font-family:'Oswald',sans-serif;color:var(--ink);font-weight:500;line-height:1;}
  .brand__name{font-size:46px;letter-spacing:1px;}
  .brand__sub{font-size:9px;letter-spacing:1px;margin-top:3px;}
  .front .brand{left:18px;top:24px;}
  .headline{position:absolute;left:18px;top:112px;font-family:'Oswald',sans-serif;color:var(--charcoal);line-height:1;}
  .headline__kicker{font-size:25px;font-weight:500;}
  .headline__main{font-size:35px;font-weight:500;margin-top:4px;}
  .tagline{position:absolute;left:18px;top:190px;width:330px;font-family:'Open Sans',sans-serif;font-size:12px;line-height:16px;color:var(--grey);}
  .services{position:absolute;left:18px;top:246px;display:grid;grid-template-columns:178px 170px;row-gap:9px;list-style:none;}
  .service{display:flex;align-items:center;gap:10px;font-family:'Roboto Condensed',sans-serif;font-weight:700;font-size:14.5px;color:var(--charcoal);height:22px;}
  .service__icon{width:23px;height:23px;border-radius:50%;background:var(--ink);display:flex;align-items:center;justify-content:center;}
  .service__icon i{width:9px;height:9px;background:var(--yellow);border-radius:2px;display:block;}
  .call{position:absolute;display:flex;align-items:center;gap:10px;font-family:'Oswald',sans-serif;font-weight:500;font-size:26px;line-height:1;white-space:nowrap;}
  .call svg{width:20px;height:22px;flex:none;}
  .front .call{left:18px;top:405px;color:var(--ink);}
  .web{position:absolute;font-family:'Open Sans',sans-serif;font-weight:700;font-size:12.5px;color:var(--ink);white-space:nowrap;}
  .front .web{left:22px;top:452px;}
  .back .web{right:16px;top:451px;}
  .back-photo{position:absolute;left:0;top:0;width:357px;height:150px;background:linear-gradient(120deg,#b99f86 0%,#e9e1d5 45%,#d9c9a6 75%,#8d9a6b 100%);}
  .intro{position:absolute;left:0;top:150px;width:357px;height:162px;background:linear-gradient(180deg,#2d2d2d,#0f0f0f);}
  .intro__title{position:absolute;left:20px;top:14px;font-family:'Oswald',sans-serif;font-weight:500;font-size:19.5px;color:var(--yellow);white-space:nowrap;}
  .intro__sub{position:absolute;left:20px;top:44px;font-family:'Open Sans',sans-serif;font-size:12px;color:#fff;}
  .feature{position:absolute;top:75px;width:90px;margin-left:-45px;text-align:center;font-family:'Open Sans',sans-serif;font-size:9.5px;color:#fff;}
  .feature svg{display:block;margin:0 auto 8px;width:44px;height:40px;}
  .about-tab{position:absolute;left:0;top:308px;padding:3px 20px 0 20px;height:26px;font-family:'Oswald',sans-serif;font-weight:500;font-size:17px;color:var(--ink);}
  .about-text{position:absolute;left:24px;top:341px;width:332px;font-family:'Open Sans',sans-serif;font-size:11px;line-height:15.5px;color:var(--ink);text-align:justify;}
  .back .brand{left:420px;top:38px;gap:10px;}
  .back .brand__mark{width:30px;height:30px;}
  .back .brand__name{font-size:36px;}
  .back .brand__sub{font-size:7px;}
  .stamp{position:absolute;left:642px;top:18px;width:96px;height:66px;border:1px solid var(--rule);}
  .address-line{position:absolute;left:412px;width:326px;height:0;border-top:1px solid var(--rule);}
  .back .call{left:424px;top:410px;color:#fff;font-size:23px;gap:8px;}
  .back .call svg{width:18px;height:20px;}
</style>
</head>
<body>
<main class="canvas">

  <section class="card card--front front">
    <svg class="shapes" width="756" height="474" viewBox="0 0 756 474">
      <defs>
        <linearGradient id="houseTones" x1="0" y1="0" x2="0" y2="1">
          <stop offset="0" stop-color="#b9cfe6"/>
          <stop offset="0.3" stop-color="#8a8579"/>
          <stop offset="0.7" stop-color="#7b7366"/>
          <stop offset="1" stop-color="#5e8a3c"/>
        </linearGradient>
      </defs>
      <polygon points="345,0 756,0 756,17 404,17 372,125" fill="var(--yellow)"/>
      <polygon points="318,474 366,396 420,396 392,474" fill="var(--ink)"/>
      <g role="img" aria-label="Photo of a two-storey suburban house with a green front lawn">
        <polygon points="404,17 756,17 756,458 388,458 414,396 372,300 392,150" fill="url(#houseTones)"/>
      </g>
      <polygon points="0,396 378,396 360,440 0,440" fill="var(--yellow)"/>
    </svg>

    <div class="brand">
      <span class="brand__mark"></span>
      <div class="brand__text">
        <div class="brand__name">HALDEN</div>
        <div class="brand__sub">PROPERTY MANAGEMENT LLC.</div>
      </div>
    </div>

    <h1 class="headline">
      <div class="headline__kicker">FULL-SERVICE</div>
      <div class="headline__main">PROPERTY MANAGEMENT</div>
    </h1>
    <p class="tagline">Maximize your financial returns with support from our rental specialists</p>

    <ul class="services">
      <li class="service"><span class="service__icon"><i></i></span>TENAT SCREENING</li>
      <li class="service"><span class="service__icon"><i></i></span>MANAGEMENT</li>
      <li class="service"><span class="service__icon"><i></i></span>RENT COLLECTION</li>
      <li class="service"><span class="service__icon"><i></i></span>ACCOUNTING</li>
      <li class="service"><span class="service__icon"><i></i></span>MAINTENANCE</li>
      <li class="service"><span class="service__icon"><i></i></span>HOA COMPLANCE</li>
      <li class="service"><span class="service__icon"><i></i></span>LEASING</li>
      <li class="service"><span class="service__icon"><i></i></span>24/7 SUPPORT</li>
    </ul>

    <div class="call"><span>CALL US NOW</span>
      <svg viewBox="0 0 20 22"><rect x="4" y="1" width="12" height="20" rx="2" fill="currentColor"/><rect x="6.5" y="4" width="7" height="11" fill="var(--yellow)"/></svg>
      <span>(012) 555-0190</span></div>
    <div class="web">www.haldenmanagement.com</div>
  </section>

  <section class="card card--back back">
    <div class="back-photo" role="img" aria-label="Photo of three people reviewing documents together in a bright living room"></div>

    <svg class="shapes" width="756" height="474" viewBox="0 0 756 474">
      <polygon points="0,316 360,316 440,420 420,474 0,474" fill="var(--yellow)"/>
      <polygon points="572,390 756,390 756,402 564,402" fill="var(--yellow)"/>
      <polygon points="418,402 756,402 756,444 398,444" fill="var(--ink)"/>
      <polygon points="0,306 172,306 178,334 0,334" fill="var(--yellow-deep)"/>
    </svg>

    <div class="intro">
      <div class="intro__title">YOUR HOME. YOUR PROJECTS. SIMPLIFIED.</div>
      <div class="intro__sub">We serve landlords and tenants</div>
      <div class="feature" style="left:71px">
        <svg viewBox="0 0 44 40"><polygon points="22,4 2,20 8,20 8,36 36,36 36,20 42,20" fill="#fff"/></svg>
        PROPERTIES</div>
      <div class="feature" style="left:176px">
        <svg viewBox="0 0 44 40"><rect x="19" y="0" width="7" height="40" fill="#fff" transform="rotate(45 22 20)"/><rect x="19" y="0" width="7" height="40" fill="#fff" transform="rotate(-45 22 20)"/></svg>
        PROJECTS</div>
      <div class="feature" style="left:287px">
        <svg viewBox="0 0 44 40" fill="#fff"><circle cx="10" cy="14" r="5"/><circle cx="34" cy="14" r="5"/><circle cx="22" cy="10" r="6"/><path d="M1 34a9 9 0 0 1 18 0z"/><path d="M25 34a9 9 0 0 1 18 0z"/><path d="M11 36a11 11 0 0 1 22 0z"/></svg>
        PARTNERS</div>
    </div>

    <div class="about-tab">ABOUT US</div>
    <p class="about-text">Our standardized full-service property management program is specifically designed for owners who want to enjoy the benefits of home ownership, but do not want the hassle of dealing with all of the day-to-day demands required to successfully manage the hassle of it all. Why worry about managing your estate, let a property management professional do it.</p>

    <div class="brand">
      <span class="brand__mark"></span>
      <div class="brand__text">
        <div class="brand__name">HALDEN</div>
        <div class="brand__sub">PROPERTY MANAGEMENT LLC.</div>
      </div>
    </div>
    <div class="stamp"></div>
    <div class="address-line" style="top:163px"></div>
    <div class="address-line" style="top:202px"></div>
    <div class="address-line" style="top:241px"></div>
    <div class="address-line" style="top:282px"></div>

    <div class="call"><span>CALL US NOW</span>
      <svg viewBox="0 0 20 22"><rect x="4" y="1" width="12" height="20" rx="2" fill="currentColor"/><rect x="6.5" y="4" width="7" height="11" fill="var(--ink)"/></svg>
      <span>(012) 555-0190</span></div>
    <div class="web">www.haldenmanagement.com</div>
  </section>

</main>
</body>
</html>
```